2019 CD Cover Design - Drifting Past Noon

Please Use Uploaded Photo. Feel free to crop and otherwise edit the photo to enrich the design. Title is "Drifting Past Noon" and should be relative prominent in the cover. Artist names are "Marcus Pellham and Rosalind Quaye" and should also be printed on the cover. Please ensure compliance with DiscHarbor Published Requirements, ie CMYK, 300dpi, etc. Planning on giving winner the Back Cover and Inside designs.

Target Market(s)

The album is a set of cover love songs, all duets, many are contemporary country, ie in the style of Copper Wagonwheel, Greta Voss, Harlow Junction. Feel free to innovate!

Industry/Entity Type

Music Download

Colors

Designer to choose colors to be used in the design.

Requirements
Nice to have
• Optional - Third Line of Text - “Contemporary Country Duets”
Should not have
• Please do NOT cut out and completely replace the grassy field background. The CD liner notes will discuss the photo, which is a renowned national park in our hometown.

```html
<!DOCTYPE html>
<html lang="en">
<head>
<meta charset="utf-8">
<title>Drifting Past Noon — Marcus Pellham &amp; Rosalind Quaye</title>
<link rel="stylesheet" href="https://fonts.googleapis.com/css2?family=Playfair+Display:wght@400;600&family=Roboto:wght@400;500;700&display=swap">
<style>
  :root {
    --field-gold: #c9a248;
    --field-light: #dcc078;
    --field-green: #8d9c4e;
    --hair-silver: #d9d8d2;
    --hair-blonde: #b89a62;
    --shirt-grey: #5a6678;
    --top-black: #1a1718;
    --night: #121213;
    --ink-white: #ffffff;
    --accent-red: #e23a22;
  }
  html, body {
    margin: 0;
    padding: 0;
    width: 1200px;
    height: 1083px;
    overflow: hidden;
    background: var(--night);
  }
  .cover {
    position: relative;
    width: 1200px;
    height: 1083px;
    overflow: hidden;
  }
  .cover-photo {
    position: absolute;
    inset: 0;
    background:
      radial-gradient(ellipse 300px 160px at 360px 200px, rgba(217,216,210,0.85), rgba(217,216,210,0) 75%),
      radial-gradient(ellipse 230px 260px at 360px 420px, rgba(206,170,150,0.55), rgba(206,170,150,0) 75%),
      radial-gradient(ellipse 420px 360px at 260px 760px, rgba(90,102,120,0.95), rgba(90,102,120,0) 78%),
      radial-gradient(ellipse 330px 520px at 820px 640px, rgba(184,154,98,0.85), rgba(184,154,98,0) 75%),
      radial-gradient(ellipse 180px 240px at 800px 560px, rgba(214,178,160,0.55), rgba(214,178,160,0) 75%),
      radial-gradient(ellipse 520px 300px at 900px 1000px, rgba(26,23,24,0.95), rgba(26,23,24,0) 80%),
      radial-gradient(ellipse 260px 420px at 1150px 400px, rgba(141,156,78,0.7), rgba(141,156,78,0) 80%),
      linear-gradient(170deg, var(--field-light) 0%, var(--field-gold) 45%, #a88e46 75%, #4a4536 100%);
  }
  .cover-shade {
    position: absolute;
    left: 0; right: 0; bottom: 0;
    height: 200px;
    background: linear-gradient(to bottom, rgba(18,18,19,0) 0%, rgba(18,18,19,0.75) 100%);
  }
  .format-mark {
    position: absolute;
    top: 52px;
    right: 42px;
    display: flex;
    align-items: center;
    gap: 10px;
    font-family: "Roboto", sans-serif;
    font-weight: 700;
    font-size: 22px;
    letter-spacing: 0.5px;
    text-transform: uppercase;
    color: var(--ink-white);
  }
  .format-mark .dot {
    width: 20px; height: 20px;
    border-radius: 50%;
    background: var(--ink-white);
  }
  .album-title {
    position: absolute;
    left: 0; top: 700px;
    width: 1200px;
    height: 260px;
  }
  .album-title text {
    font-family: "Playfair Display", serif;
    font-weight: 600;
    fill: var(--ink-white);
  }
  .album-title .title-joiner { fill: var(--accent-red); font-weight: 400; }
  .album-title .title-rule { fill: var(--ink-white); }
  .album-subtitle {
    position: absolute;
    left: 87px;
    top: 924px;
    margin: 0;
    font-family: "Roboto", sans-serif;
    font-size: 21px;
    line-height: 26px;
    color: var(--ink-white);
  }
  .album-artists {
    position: absolute;
    left: 86px;
    top: 958px;
    margin: 0;
    font-family: "Roboto", sans-serif;
    font-size: 36px;
    line-height: 42px;
    letter-spacing: 0.6px;
    text-transform: uppercase;
    color: var(--ink-white);
    white-space: nowrap;
  }
</style>
</head>
<body>
<main class="cover">
  <div class="cover-photo" role="img" aria-label="Photograph of the two duet singers, a grey-haired man in a grey shirt and a woman with long wavy blonde hair in a black top, posed in a golden grassy field of the hometown national park"></div>
  <div class="cover-shade"></div>

  <div class="format-mark"><span class="dot"></span>SoundPlate Audio</div>

  <svg class="album-title" viewBox="0 0 1200 260" role="img" aria-label="Drifting Past Noon">
    <text x="87" y="208" font-size="205" textLength="380" lengthAdjust="spacingAndGlyphs">Drifting</text>
    <text class="title-joiner" x="474" y="182" font-size="66" textLength="52" lengthAdjust="spacingAndGlyphs">Past</text>
    <text x="532" y="208" font-size="205" textLength="256" lengthAdjust="spacingAndGlyphs">Noon.</text>
    <rect class="title-rule" x="436" y="227" width="348" height="5"/>
  </svg>

  <p class="album-subtitle">Contemporary Country Duets</p>
  <p class="album-artists">Marcus Pellham &amp; Rosalind Quaye</p>
</main>
</body>
</html>
```